Digital Imaging Website Design Project

This project is for 3 page designs - The main Home page design, department page design & content page design which will utilize most of the home page components.

Client Background - http://www.kelrofab.com

An almost Forty year old established printing company that has a large client base of architect/engineering, as the print shop opened up as a blueprinting company, and over the years has grown, changed and expanded to offer document and digital file management for this industry. KRFab. has also always offered color printing services, but recently has expanded their color department to be able to offer amazing dimensional printing, and extreme cutting technology.

These new products and services will be targeted to new industries for repeatable printing needs, promotional, point of purchase color printing, as well as in-store, interior decor/wall. These new printing services are only offered by KRFAB in their area, and they want to convey that they are on the leading edge of color printing technology, while at the same time, not eliminating their existing primary business scaring away their traditional client base of architectural/engineering firms that use them for large format printing, scanning and document management services.

1 - Home Page Design
Primary Goals of the design:

1.Provide a new, eye catching engaging website that conveys the above expansion/growth/cutting edge company.
2.Full screen design please to move away from the 'center' bordered up website they currently have.
3.Design Components – We don't have any media to provide you with exception of our logo. We're looking for fresh design that is exciting and engaging imagery. Additionally, we are working on a color/effected version of our logo to place on the color division page, and this will probably tie in with the design you create for us.
4.It should be designed to be able to work as a responsive design as well so that when installed, will work across devices etc..
5.Colors – Same color scheme, but if you have an accent color you'd like to use to make the site pop, go for it!

Requirements:
1.The 4 divisions of the company should be the main feature so that the client depending on which department they are needing, will see those 4 choices clearly in the design, and they'll know to click on one of them to get more information and to their needed services.

2.The main goal of the site is to get visitors to place an order, there should be a feature on the home page for this call to action.

3.Put in an element that communicates the main benefit of KRFab. - an area for a 1-line Statement/Call to Action / Overall Company Benefit/

4.The 4 divisions need to have eye catching elements related to their products and services, and that clearly illustrate that the user should click on that to go to the appropriate area for products and services

Reprographics
This department is specifically geared to architect/engineering industry
BYLine for optional Use: Partnering with Building Industry Providers since 1975
Related pages for better understanding:
http://www.kelrofab.com/services/portland_professional_printing_services
http://www.kelrofab.com/services/reprographics
Digital File Management
This department is related to Architect/engineers, but can also apply to any other industry needing electronic document management, scanning, or archival services.
BYLine for optional use: Effective & Efficient Digital Solutions at every level.
Related Pages:
http://www.kelrofab.com/colorgraphics/electronic_file_document_management
http://www.kelrofab.com/colorgraphics/document_scanning_service
http://www.kelrofab.com/services/scanning_and_archiving

Color Graphics
This Department is newly expanded / has expanded services / they are focusing more of their efforts on this department and is a key reason for updated website design.
This Department image/representation should be stellar in the imagery to convey the excellence of the color department the services availble.
One of their newest products/services is dimensional printing – not 3-D, but raised element printing. Essentially a client could pick components on their graphic that that they want to 'bump' out, and additional layers would be put in place to create a popped out, dimensional effect. * Bonus points for creating the color department image that effectively conveys this new service – whether it's showing an abstract image/element that is actually raised off the page/paper/component. Additionally the color dimensional printing can be done on practically any material – glass, vinyl, material etc.... Please let me know if you have any questions on this.
BYLine for optional Use: See How Our Color Stands Out From the Rest
Related pages:
http://www.kelrofab.com/colorgraphics
http://www.kelrofab.com/colorgraphics/color_digital_imaging

Equipment & Supplies
This department provides specific supplies and hardware vs. printing products/services. Our largest client base is architects/engineers, but is not limited to this industry. Typical equipment is large printers, and supplies are typically paper products geared to the large format printing services, for the architect/engineers industry.
Byline for optional Use: In-House Printing & Fulfillment Services
Related pages:
http://www.kelrofab.com/varlen_tusk_equipment_sales
http://www.kelrofab.com/supplies

Additionally - Possibly have descriptive text sections below these 4 elements, but this is optional.

2.) Department/Division Page design -

This page should pull the home page element to over based on which division is selected.
Have a submenu design incorporated so that users can navigate to all the products and services that will be listed under that division
Contain a plugin design for FAQs – so that depending on which division page they are on, the appropriate FAQ's would display for use to have easy access to.
Contain a plugin design for – Contact Us easy form – short form –
Name
Company
Number
Email
Project Details/Questions: Text box

3.)Content Page design
This page should have main area for content
Area for an image with slideshow of other supporting images
Optional area for video – most (99%) of the pages will not have videos, but in the case we do, would like an area that will display videos effectively.
Optional FAQ plugin display
Contact plugin display

Global Elements:

Static and very visible site features that are in a position so that if user clicks beyond home page will still see these are:
Get a Quote
Place Order
Digital Plan-room
Call Today - 503-481-7962

Other global components:
SM Icons – QN, Chirpo, WorkLoop
Rotating Testimonial

Navigational Menu:
The KRF Difference
About
Sustainability
Products & Services
Reprograhics
Digital File Management
Color Graphics
Equipment & Supplies
Login
Blog
Contact Us

After the contest – What would be great to have is when a user clicks on one of the departments, it takes that visual element and continues onto it's department page for a smaller but related image - But this may be an after this web design contest.

Additionally will need some other design work on the interior pages, as well, so hoping to find a great designer to complete the other tasks – as well as be the go-to for future endeavors!

Thanks for looking at the project, and I look forward to any questions you may have.
Updates

Looking forward to hearing from interested designers! - If you're curious about my work, you can find my profile at:  https://www.gigmarla.com/users/~07b3e2f95d18c4a260

Target Market(s)

Please see description

Industry/Entity Type

Electronic

Requirements
Must have
• Please see description

```html
<!DOCTYPE html>
<html lang="en">
<head>
<meta charset="utf-8">
<title>KRFab. Digital Imaging – Divisions</title>
<link rel="stylesheet" href="https://fonts.googleapis.com/css2?family=Titillium+Web:wght@400;600&family=Arimo:wght@400&display=swap">
<style>
  :root {
    --page-dark: #2f3132;
    --panel-light: #f3f3f3;
    --panel-white: #f7f7f7;
    --ink: #111;
    --body-grey: #5f5f5f;
    --accent-blue: #1f8fe0;
    --accent-orange: #f28a12;
    --menu-bg: #2b2b2b;
    --menu-text: #f2f2f2;
    --footer-dark: #1f1f1f;
    --footer-darker: #181818;
  }
  html, body { margin: 0; padding: 0; overflow: hidden; }
  body { width: 1200px; height: 846px; background: var(--page-dark); }
  .canvas {
    position: relative; width: 1200px; height: 846px; overflow: hidden;
    background: linear-gradient(135deg, #3a3c3d 0%, #2a2c2d 60%, #303233 100%);
  }
  .division-grid {
    position: absolute; left: 74px; top: 0; width: 1126px; height: 721px;
    background: var(--panel-light);
  }
  .division-text {
    position: absolute; width: 300px;
    font-family: "Arimo", Arial, sans-serif; font-size: 16px; line-height: 29.6px;
    color: var(--body-grey);
  }
  .division-text p { margin: 0; }
  .division-title {
    font-family: "Titillium Web", sans-serif; font-weight: 600;
    font-size: 23.5px; line-height: 32px; margin: 0 0 26px; color: var(--ink);
  }
  .division-title .accent-blue { color: var(--accent-blue); }
  .division-title .accent-orange { color: var(--accent-orange); }
  .visual { position: absolute; }
  .visual-reprographics {
    left: 357px; top: 0; width: 356px; height: 320px;
    background: linear-gradient(160deg, #e9e9e9 0%, #ffffff 40%, #c9b08a 55%, #6d6d6d 70%, #f2f2f2 100%);
  }
  .visual-color {
    left: 357px; top: 320px; width: 356px; height: 401px;
    background: linear-gradient(180deg, #2f9fe6 0%, #bfe2f7 35%, #f5f8fb 50%, #7fc24a 75%, #c9cfcf 100%);
  }
  .visual-edge-top {
    left: 1070px; top: 200px; width: 56px; height: 120px;
    background: linear-gradient(180deg, #1c8f9c 0%, #9ad4d8 60%, #e8f3f4 100%);
  }
  .visual-equipment {
    left: 1070px; top: 320px; width: 56px; height: 401px;
    background: linear-gradient(180deg, #ffffff 0%, #dfe3e4 40%, #8f9798 70%, #c9ced0 100%);
  }
  .product-menu {
    position: absolute; left: 900px; top: 0; width: 292px; height: 208px;
    background: var(--menu-bg); margin: 0; padding: 0 26px 0 36px; box-sizing: border-box;
    list-style: none;
  }
  .product-menu li {
    font-family: "Titillium Web", sans-serif; font-size: 17px; color: var(--menu-text);
    height: 64px; line-height: 44px; border-bottom: 1px dashed #5c5c5c;
    padding-top: 0;
  }
  .product-menu li:first-child { height: 52px; line-height: 42px; }
  .product-menu li:last-child { border-bottom: none; }
  .site-footer { position: absolute; left: 74px; top: 721px; width: 1126px; height: 125px; }
  .footer-nav {
    position: absolute; left: 0; top: 0; width: 272px; height: 125px;
    background: var(--footer-darker); margin: 0; padding: 0; list-style: none;
  }
  .footer-nav li {
    font-family: "Titillium Web", sans-serif; font-size: 17.5px; color: var(--menu-text);
    padding-left: 35px; height: 80px; line-height: 100px; border-bottom: 1px solid #3a3a3a;
  }
  .footer-nav li + li { line-height: 70px; border: none; }
  .benefits {
    position: absolute; left: 272px; top: 0; width: 429px; height: 125px;
    background: var(--footer-dark); padding: 14px 0 0 23px; box-sizing: border-box;
    font-family: "Titillium Web", sans-serif; font-size: 23px; line-height: 44px;
    color: var(--accent-blue);
  }
  .benefits p { margin: 0; }
  .benefits .list-start { font-family: "Arimo", Arial, sans-serif; font-size: 15px; color: #ddd; margin-top: 4px; }
  .benefit-bar { position: absolute; left: 701px; top: 0; width: 12px; height: 125px; background: var(--accent-blue); }
  .testimonial {
    position: absolute; left: 713px; top: 0; width: 413px; height: 125px;
    background: var(--panel-white); padding: 68px 0 0 113px; box-sizing: border-box;
    font-family: "Titillium Web", sans-serif; font-size: 17px; color: #222; line-height: 40px;
  }
  .testimonial p { margin: 0; }
</style>
</head>
<body>
<main class="canvas">
  <section class="division-grid">
    <div class="division-text" style="left:35px; top:-22px;">
      <h2 class="division-title"><span class="accent-blue">Industry Providers since 1975</span></h2>
      <p>At Kelro Print and Fabrication we provide a wide array of services involv­ing document imaging and duplication as well as online and offline document management and archiving services.</p>
    </div>

    <div class="visual visual-reprographics" role="img" aria-label="Cutaway model of a house under construction resting on architectural blueprints"></div>

    <div class="division-text" style="left:747px; top:-22px;">
      <h2 class="division-title"><span class="accent-orange">Solutions at every level</span></h2>
      <p>We have online document man­agement solutions for both physical and digital files, and/or your own archive, the system can scale, and you can grow.</p>
    </div>

    <div class="visual visual-edge-top" role="img" aria-label="Edge of a teal color graphics image"></div>

    <div class="division-text" style="left:37px; top:352px;">
      <h2 class="division-title">See How Our Color Stands<br><span class="accent-orange">Out From the Rest</span></h2>
      <p>We have been delivering an array of high quality color imaging and finish­ing services for over 35 years. Throughout our history, KP&amp;F has grown its product and service offer­ings in response to our client's ex­panding requirements......</p>
    </div>

    <div class="visual visual-color" role="img" aria-label="Stack of printed sheets with a raised landscape of grass, a tree, a city skyline and hot air balloons in a blue sky"></div>

    <div class="division-text" style="left:747px; top:352px; width:330px;">
      <h2 class="division-title">In-House Printing &amp;<br><span class="accent-blue">Fulfillment Services</span></h2>
      <p>Kelro Print &amp; Fabrication is Oregon's premier Varlen and Tusk Authorized Ser­vicing Reseller. We offer a complete end-to-end solution including equipment consultation, service, media selection, and cost recovery. Purchase, lease, or let us customize....</p>
    </div>

    <div class="visual visual-equipment" role="img" aria-label="Large format printer with control panel"></div>
  </section>

  <ul class="product-menu">
    <li>DIGITAL FILE MANAGEMENT</li>
    <li>COLOR GRAPHICS</li>
    <li>EQUIPMENT &amp; SUPPLIES</li>
  </ul>

  <footer class="site-footer">
    <ul class="footer-nav">
      <li>ABOUT KELRO PRINT</li>
      <li>TO OUR CUSTOMERS</li>
    </ul>
    <div class="benefits">
      <p>As a customer of Kelro Print &amp; Fabri-<br>cation, your benefits include:</p>
      <p class="list-start">• Accurate, on-time and fully managed print jobs</p>
    </div>
    <div class="benefit-bar"></div>
    <div class="testimonial">
      <p>content -- TBD</p>
      <p>Request Name?</p>
    </div>
  </footer>
</main>
</body>
</html>
```